Consulting Executive Needs Personal InfoGraphic One Pager

I need a one-page personal promo piece which contains a number of infographics highlighting core aspects of my professional experience and qualifications. This is meant to visually illustrate the talents and background I can bring to prospective employers. The final design must fit onto on standard U.S. Letter size page, include the categories of information I want represented in "mini infographics", and be a bit fun and quirky. No restriction on color scheme, though I do love purple and would be happy to see that as a primary color. I'm providing a spec which lists out which information needs to be included.

Industry/Entity Type

Consulting

Requirements
Must have
• Must fit onto a single U.S. letter size page (8.5" x 11")

```html
<!DOCTYPE html>
<html lang="en">
<head>
<meta charset="utf-8">
<title>J. Morgan Ellery — Personal Infographic</title>
<link rel="stylesheet" href="https://fonts.googleapis.com/css2?family=Roboto+Condensed:wght@300;400;700&display=swap">
<style>
:root{
  --bg:#252320;
  --lime:#33cc47;
  --lime-deep:#23a135;
  --olive:#4f7a1c;
  --leaf:#76bc21;
  --leaf-band:#4f8a1d;
  --forest:#3d5a12;
  --grey:#97928f;
  --accent:#3ddc45;
  --side:#4ccc4c;
  --white:#ffffff;
  --mail:#c03ad8;
}
*{margin:0;padding:0;box-sizing:border-box}
html,body{width:927px;height:1200px;overflow:hidden;background:var(--bg)}
body{font-family:"Roboto Condensed","Arial Narrow",sans-serif}
.canvas{position:relative;width:927px;height:1200px;background:var(--bg)}
.shapes{position:absolute;inset:0}
.name{font-family:"Roboto Condensed",sans-serif;font-weight:700;font-size:23px;fill:var(--white)}
.block{position:absolute;text-align:center;line-height:18.3px;font-size:14.5px;font-weight:300}
.role{position:absolute;width:84px;text-align:center;color:var(--white);font-size:17px;line-height:21.5px;font-weight:300;transform:translate(-50%,-50%)}
.contact{left:298px;top:279px;width:300px;color:var(--white);font-size:15px;line-height:20.3px;font-weight:300}
.contact .mail{color:var(--mail)}
.clients{left:238px;top:515px;width:420px;color:var(--white)}
.section-label{font-weight:700;color:var(--white)}
.platform{position:absolute;left:248px;top:664px;width:400px;text-align:center;color:var(--white);font-weight:700;font-size:29px;line-height:36px}
.modules{left:238px;top:711px;width:420px;color:var(--white)}
.leadership{left:280px;top:887px;width:336px;color:var(--white)}
.leadership h2{font-size:21.5px;line-height:28px;font-weight:700;margin-bottom:-2px}
.side{color:var(--side)}
.side h2{color:var(--accent);font-weight:700}
.side .big{font-size:30px;line-height:29px}
.side .mid{font-size:22px;line-height:26px;margin-bottom:-3px}
.side .sub{color:var(--accent);font-size:14px;font-weight:700;line-height:17px;margin-bottom:6px}
.sales{left:43px;top:538px;width:200px}
.sales h2{margin-bottom:8px}
.consult{left:665px;top:537px;width:200px}
.talents{left:43px;top:918px;width:200px}
.offer{left:615px;top:918px;width:300px}
</style>
</head>
<body>
<div class="canvas">
  <svg class="shapes" width="927" height="1200" viewBox="0 0 927 1200">
    <defs>
      <clipPath id="leaf-clip"><circle cx="448" cy="666" r="209"/></clipPath>
      <path id="name-arc" d="M 268,239 A 180,180 0 0 1 628,239"/>
    </defs>
    <circle cx="448" cy="1006" r="167" fill="var(--forest)"/>
    <circle cx="448" cy="666" r="209" fill="var(--leaf)"/>
    <rect x="230" y="665" width="440" height="35" fill="var(--leaf-band)" clip-path="url(#leaf-clip)"/>
    <circle cx="448" cy="239" r="224" fill="var(--lime)"/>
    <path d="M310,262 L586,262 A140,140 0 0 1 310,262 Z" fill="var(--lime-deep)"/>
    <circle cx="255" cy="125" r="51" fill="var(--olive)"/>
    <circle cx="639" cy="125" r="51" fill="var(--olive)"/>
    <circle cx="255" cy="352" r="51" fill="var(--olive)"/>
    <circle cx="639" cy="352" r="51" fill="var(--olive)"/>
    <circle cx="448" cy="461" r="51" fill="var(--olive)"/>
    <text class="name"><textPath href="#name-arc" startOffset="50%" text-anchor="middle">J. Morgan Ellery</textPath></text>
    <rect x="398" y="105" width="100" height="140" rx="20" fill="#5fdc6f" role="img" aria-label="Figure with raised arms"/>
    <circle cx="143" cy="482" r="39" fill="var(--grey)" role="img" aria-label="Sales icon"/>
    <circle cx="765" cy="479" r="39" fill="var(--grey)" role="img" aria-label="Consulting icon"/>
    <circle cx="143" cy="867" r="39" fill="var(--grey)" role="img" aria-label="Summit icon"/>
    <circle cx="765" cy="867" r="39" fill="var(--grey)" role="img" aria-label="Meeting icon"/>
    <circle cx="448" cy="1145" r="39" fill="var(--grey)" role="img" aria-label="Team icon"/>
  </svg>

  <div class="role" style="left:255px;top:125px">Project Director</div>
  <div class="role" style="left:639px;top:125px">Project Rescue</div>
  <div class="role" style="left:255px;top:352px">Program Manager</div>
  <div class="role" style="left:639px;top:352px">Clinical Process Redesign</div>
  <div class="role" style="left:448px;top:461px">Executive Advisor</div>

  <div class="block contact">
    417 Larkspur Lane, Oakland, CA 94610<br>
    <span class="mail">morgan_ellery@mail.example</span><br>
    mobile: 510.555.0142
  </div>

  <div class="block clients">
    Tallowbrook Clinic | QVRN<br>
    Halvorsen | Gulfcoast Hospitals | University of Bayview<br>
    Marrowind Health | Plains Children’s Hospital<br>
    Children’s Lakeview Hospital | University of Northport<br>
    Pellcrest University | Brennick Hospitals | University of Ozark Valley<br>
    St. Ansel’s Harbor | Keller Permanent<br>
    <span class="section-label" style="display:block;margin-top:13px">Implementation Experience</span>
  </div>

  <div class="platform">Helix</div>

  <div class="block modules">
    <span class="section-label" style="display:block;margin-bottom:19px">Application Expertise</span>
    HelixCare Ambulatory | HelixCare Inpatient Clin Doc and Orders<br>
    MyRecord | Cadenza | Overture/ADT | Rapid | Optiva<br>
    Aspen | Lantern | Steadfast HB &amp; PB | Heron<br>
    Nurse Triage | Care Anywhere<br>
    Health Link | Lumen
  </div>

  <div class="block leadership">
    <h2>Leadership<br>&amp; Staff Management</h2>
    20+ years team building &amp;<br>
    staff management expertise<br>
    Number of times staff have told me<br>
    “You are the best boss ever”: countless<br>
    Developed leadership development programs<br>
    or conducted leadership courses for 6 corporations,<br>
    including Northline &amp; Kaizo<br>
    Certified in Keller-Brandt and other<br>
    leadership/personality assessments
  </div>

  <div class="block side sales">
    <h2 class="big">Sales<br>Experience</h2>
    Nation Helix Sales VP for<br>
    Norvane Health<br>
    Client Executive<br>
    for Caredex<br>
    Average $2M in monthly<br>
    consulting services sales<br>
    for Norvane Health<br>
    Sales strategy architect<br>
    for Norvane Health<br>
    Make immediate connections<br>
    with prospects = sold work
  </div>

  <div class="block side consult">
    <h2 class="big">Consulting</h2>
    <p class="sub">Firm Start Up Stats</p>
    Number of firms built from<br>
    the ground floor:<br>
    4<br>
    Number of business<br>
    plans authored:<br>
    8<br>
    Number of marketing<br>
    plans authored:<br>
    6<br>
    Number of core consulting<br>
    methodologies developed:<br>
    4
  </div>

  <div class="block side talents">
    <h2 class="mid">Random Talents</h2>
    Attended clown college<br>
    15+ years graphic design &amp;<br>
    web development experience<br>
    Free therapy!<br>
    (clinical psychologist and<br>
    prior family therapist)
  </div>

  <div class="block side offer">
    <h2 class="mid">What Can I Do for You?</h2>
    Recruit and inspire high performing<br>
    consulting teams. Build and sustain growth of your<br>
    consulting business Sell, sell, sell current<br>
    and prospective clients on your services<br>
    Develop and implement business and marketing<br>
    plans Deliver top quality consulting<br>
    services<br>
    Make work fun
  </div>
</div>
</body>
</html>
```